Vellorin - Business Cards for a new venture

create business card for a startup classified business dealing in construction materials, the cards need to have a professional look but modern, more serious than playful, one of the samples must include the official font (attached), please explore using the official colors in the company's logo

Target Market(s)

Energy sector

Contact Information for Business Card

Font styles to use
Other font styles liked:
• suissnord

Requirements
Must have
• corporate colors (in logo attached)
Nice to have
• Official font (in one of the samples) font is : suissnord
Should not have
• Cartoonish look

```html
<!DOCTYPE html>
<html lang="en">
<head>
<meta charset="UTF-8">
<title>Vellorin – Business Cards</title>
<link href="https://fonts.googleapis.com/css2?family=Michroma&display=swap" rel="stylesheet">
<style>
  :root {
    --backdrop: #3a4355;
    --card: #ffffff;
    --navy: #1d4a86;
    --grey: #9b9b9b;
    --card-shadow: rgba(10, 14, 24, 0.45);
  }
  * { box-sizing: border-box; margin: 0; padding: 0; }
  html, body {
    width: 1200px;
    height: 1200px;
    overflow: hidden;
    background: var(--backdrop);
    font-family: "Michroma", sans-serif;
  }
  .card {
    position: absolute;
    width: 760px;
    height: 430px;
    background: var(--card);
    border-radius: 36px;
    box-shadow: 0 18px 40px var(--card-shadow);
  }
  .card--front { left: 110px; top: 140px; }
  .card--back  { left: 330px; top: 630px; }

  .brand {
    display: flex;
    align-items: center;
    gap: 22px;
  }
  .brand__mark {
    background: var(--navy);
    border-radius: 50%;
  }
  .brand__name {
    color: var(--navy);
    letter-spacing: 0.12em;
    text-transform: uppercase;
    font-weight: 400;
  }

  .card--front .brand {
    position: absolute;
    inset: 0;
    justify-content: center;
  }
  .card--front .brand__mark { width: 44px; height: 44px; }
  .card--front .brand__name { font-size: 52px; }

  .card--back .brand {
    position: absolute;
    left: 60px;
    top: 0;
    height: 100%;
    width: 300px;
    justify-content: center;
    gap: 14px;
  }
  .card--back .brand__mark { width: 26px; height: 26px; }
  .card--back .brand__name { font-size: 30px; }

  .divider {
    position: absolute;
    left: 380px;
    top: 40px;
    width: 2px;
    height: 350px;
    background: var(--navy);
  }

  .contact {
    position: absolute;
    left: 412px;
    top: 58px;
    right: 30px;
    color: var(--navy);
  }
  .contact__name {
    font-size: 21px;
    line-height: 1.2;
    text-transform: capitalize;
  }
  .contact__name span { color: var(--grey); }
  .contact__role {
    font-size: 13px;
    margin-top: 8px;
    text-transform: capitalize;
  }
  .contact__list {
    list-style: none;
    margin-top: 26px;
  }
  .contact__item {
    display: flex;
    align-items: center;
    gap: 14px;
    font-size: 15px;
    margin-bottom: 16px;
  }
  .contact__item svg { width: 22px; height: 22px; flex: none; fill: var(--navy); }
  .contact__address {
    margin-top: 22px;
    font-size: 11px;
    line-height: 1.9;
    text-transform: capitalize;
  }
</style>
</head>
<body>

  <section class="card card--front" aria-label="Business card front">
    <div class="brand">
      <span class="brand__mark"></span>
      <span class="brand__name">Vellorin</span>
    </div>
  </section>

  <section class="card card--back" aria-label="Business card back">
    <div class="brand">
      <span class="brand__mark"></span>
      <span class="brand__name">Vellorin</span>
    </div>

    <div class="divider"></div>

    <div class="contact">
      <p class="contact__name">Name of <span>person</span></p>
      <p class="contact__role">Designation</p>
      <ul class="contact__list">
        <li class="contact__item">
          <svg viewBox="0 0 24 24" aria-hidden="true"><path d="M3 9c0-3 4-5 9-5s9 2 9 5v2h-5V9c-1-1-7-1-8 0v2H3zM6 12h12l2 8H4z"/></svg>
          +123 456 789
        </li>
        <li class="contact__item">
          <svg viewBox="0 0 24 24" aria-hidden="true"><path d="M7 2h10a2 2 0 0 1 2 2v16a2 2 0 0 1-2 2H7a2 2 0 0 1-2-2V4a2 2 0 0 1 2-2zm0 3v13h10V5zm5 14.2a1 1 0 1 0 0 .1z"/></svg>
          +123 456 789
        </li>
        <li class="contact__item">
          <svg viewBox="0 0 24 24" aria-hidden="true"><path d="M2 5h20v14H2zm2 2v.5l8 5 8-5V7zm0 3v7h16v-7l-8 5z"/></svg>
          name@email.com
        </li>
      </ul>
      <p class="contact__address">No.01, Adrs line 01,<br>Adrs line 02, City, Country.</p>
    </div>
  </section>

</body>
</html>
```